DOG DAYCARE BILLBOARD

Design a bold exciting billboard that can be read easily from a distance! Our goal is brand awareness and showcasing the services we offer (Boarding, Grooming, Daycare, and Training.
we would like to see examples with the phrase "your best friend's best day". Our name Bright Meadow Canine Activity Center (or just Bright Meadow might work better and could be bigger) and the services we provide.
(there are two examples of what we like included in the pictures)
you can find more information o our website at pawplayhub@mailnest.example.

```html
<!DOCTYPE html>
<html lang="en">
<head>
<meta charset="utf-8">
<title>Bright Meadow Canine Activity Center – Billboard</title>
<link rel="stylesheet" href="https://fonts.googleapis.com/css2?family=Playfair+Display:wght@400;700;900&display=swap">
<style>
  :root {
    --stage: #5f5f5f;
    --paper: #ffffff;
    --olive: #c2b000;
    --olive-dark: #a89800;
    --leaf: #5cb800;
    --leaf-bright: #74d400;
    --ink: #1c1c1c;
    --mist: #d9d9d9;
    --coat: #e6c48a;
  }
  * { margin: 0; padding: 0; box-sizing: border-box; }
  html, body { width: 1200px; height: 900px; overflow: hidden; }
  body { background: var(--stage); font-family: "Playfair Display", Georgia, serif; position: relative; }

  .billboard {
    position: absolute; left: 93px; top: 221px; width: 1028px; height: 467px;
    background: var(--paper); overflow: hidden;
  }
  .billboard__shapes { position: absolute; inset: 0; }

  .photo-backdrop {
    position: absolute; left: 470px; top: 80px; width: 558px; height: 387px;
    background: radial-gradient(ellipse at 60% 50%, var(--mist) 0%, rgba(217,217,217,0.5) 45%, rgba(255,255,255,0) 75%);
  }
  .photo-dog {
    position: absolute; left: 95px; top: 14px; width: 275px; height: 420px;
    background: linear-gradient(180deg, #e9cf9c 0%, var(--coat) 55%, #d7b072 100%);
    border-radius: 120px 120px 40px 40px;
  }

  .brand {
    position: absolute; left: 350px; top: 58px; display: flex; align-items: center; gap: 8px;
    color: var(--ink); font-weight: 700; font-size: 21px;
  }
  .brand__dot { width: 14px; height: 14px; border-radius: 50%; background: var(--ink); }

  .headline { position: absolute; left: 617px; top: 40px; line-height: 1; font-weight: 900; text-shadow: 2px 2px 2px rgba(0,0,0,0.35); }
  .headline__line { display: block; }
  .headline__line--one { color: var(--olive); font-size: 60px; }
  .headline__line--two { color: var(--leaf); font-size: 52px; margin-top: 0; }
  .headline__line--three { color: var(--olive); font-size: 40px; margin-top: 4px; }

  .services { position: absolute; left: 497px; top: 225px; display: grid; grid-template-columns: 218px 200px; row-gap: 10px; }
  .service { display: flex; align-items: center; gap: 12px; font-weight: 700; font-size: 22px; color: var(--ink); height: 50px; }
  .service__icon { width: 50px; height: 50px; flex: none; }
  .services__divider { position: absolute; left: 189px; top: -6px; width: 2px; height: 132px; background: #555; }
  .services .service:nth-child(odd) { }

  .contact { position: absolute; left: 487px; top: 380px; color: var(--ink); font-size: 15px; line-height: 22px; }
  .contact__web { font-size: 17px; letter-spacing: 1.2px; margin-top: 2px; }

  .callout { position: absolute; left: 845px; top: 380px; color: var(--paper); }
  .callout__label { font-size: 19px; font-weight: 400; }
  .callout__phone { font-size: 23px; font-weight: 700; margin-top: 4px; }
</style>
</head>
<body>
  <main class="billboard">
    <div class="photo-backdrop" role="img" aria-label="Faded photo of playful dogs"></div>

    <svg class="billboard__shapes" width="1028" height="467" viewBox="0 0 1028 467" aria-hidden="true">
      <circle cx="225" cy="269" r="222" fill="var(--olive)"/>
      <circle cx="205" cy="285" r="205" fill="var(--paper)"/>
      <circle cx="200" cy="290" r="188" fill="var(--leaf-bright)"/>
      <rect x="0" y="350" width="420" height="117" fill="var(--leaf)"/>
      <circle cx="455" cy="70" r="150" fill="var(--leaf)"/>
      <circle cx="428" cy="52" r="142" fill="var(--paper)"/>
      <circle cx="997" cy="499" r="205" fill="var(--olive)"/>
    </svg>

    <div class="photo-dog" role="img" aria-label="Photo of a golden retriever puppy sitting on grass"></div>

    <div class="brand"><span class="brand__dot"></span><span>Bright Meadow</span></div>

    <h1 class="headline">
      <span class="headline__line headline__line--one">YOUR BEST</span>
      <span class="headline__line headline__line--two">FRIEND'S</span>
      <span class="headline__line headline__line--three">BEST DAY</span>
    </h1>

    <ul class="services">
      <li class="service">
        <svg class="service__icon" viewBox="0 0 50 50"><circle cx="25" cy="25" r="22" fill="#fff" stroke="var(--leaf)" stroke-width="3"/><rect x="13" y="18" width="24" height="14" rx="2" fill="none" stroke="var(--ink)" stroke-width="2"/></svg>
        Boarding
      </li>
      <li class="service">
        <svg class="service__icon" viewBox="0 0 50 50"><circle cx="25" cy="25" r="22" fill="#fff" stroke="var(--olive)" stroke-width="3"/><circle cx="25" cy="25" r="7" fill="var(--ink)"/></svg>
        Daycare
      </li>
      <li class="service">
        <svg class="service__icon" viewBox="0 0 50 50"><circle cx="25" cy="25" r="22" fill="#fff" stroke="var(--olive)" stroke-width="3"/><rect x="18" y="18" width="14" height="14" fill="var(--ink)"/></svg>
        Grooming
      </li>
      <li class="service">
        <svg class="service__icon" viewBox="0 0 50 50"><circle cx="25" cy="25" r="22" fill="#fff" stroke="var(--leaf)" stroke-width="3"/><path d="M15 33 L25 17 L35 33" fill="none" stroke="var(--ink)" stroke-width="2"/></svg>
        Training
      </li>
      <span class="services__divider"></span>
    </ul>

    <address class="contact" style="font-style:normal">
      <div>Bright Meadow Canine Activity Center</div>
      <div>48 Orchard Row, Millbrook, ST 00000</div>
      <div class="contact__web">www.pawplayhub.example</div>
    </address>

    <div class="callout">
      <div class="callout__label">CALL US TODAY</div>
      <div class="callout__phone">(555) 014-2876</div>
    </div>
  </main>
</body>
</html>
```